Personal Training card design

i am a enthusiastic personal trainer wanting to appeal to as many people as possible.

offering health screening, single or group personal training, geared towards helping the client achieve their goal no matter what it is.

providing a professional service in a top gym facility.

I want to come across professional and trustworthy.

I want my card to be timeless and not look out of date in a years time.

I want the card to be informative and clear about what I offer and display my contact details.

ideally id like the colours blue and white but open to other colour options.

I want the final outcome to communicate professionalism, a PT the clients can trust, and that I can do what I claim.

id like a logo similar to the picture I have provided (the logo on the left hand side) if possible incorporating my initials "OD" or "ODF" but not essential.

Industry/Entity Type

Professional Service

Contact Information for Business Card

OwenDaleyFitness

"Real Results For Every Body"

specializing in
- weight loss & tone
- strength and conditioning
- nutritional advice

Book your free consultation today and take the first step toward achieving your goal!

for details contact me via
email: owendaleyfitness.example.co.uk
phone: 07700954218

or..
visit me via
facebook: owendaleyfitness
twitter: @owendaleyfitness

```html
<!DOCTYPE html>
<html lang="en">
<head>
<meta charset="utf-8">
<title>Owen Daley Fitness – Business Card Design</title>
<link rel="stylesheet" href="https://fonts.googleapis.com/css2?family=Arimo:ital,wght@0,400;0,700;1,400&family=Russo+One&display=swap">
<style>
  :root {
    --brand-blue: #0b92dc;
    --ring-blue: #2aa6e8;
    --soft-blue: #52b6ec;
    --brand-orange: #e8891e;
    --paper: #ffffff;
    --ink: #222222;
    --card-edge: #9a9a9a;
  }
  * { box-sizing: border-box; margin: 0; padding: 0; }
  html, body {
    width: 761px; height: 1200px; overflow: hidden;
    background: var(--paper);
    font-family: "Arimo", Arial, sans-serif;
  }
  .sheet { position: relative; width: 761px; height: 1200px; }

  .side-label {
    position: absolute; left: 48px;
    font-size: 38px; color: var(--ink);
    line-height: 1; transform: translateY(-50%);
  }

  .card {
    position: absolute; left: 275px;
    width: 439px; height: 289px;
    border: 1px solid var(--card-edge);
    background: var(--paper);
    overflow: hidden;
  }
  .card-art { position: absolute; inset: 0; width: 100%; height: 100%; }

  .brand-name {
    position: absolute;
    font-family: "Arimo", Arial, sans-serif;
    font-weight: 700; color: var(--brand-orange);
    font-size: 24px; line-height: 1; white-space: nowrap;
  }
  .service-word {
    position: absolute;
    font-family: "Arimo", Arial, sans-serif;
    font-weight: 700; color: var(--paper);
    letter-spacing: 2px; line-height: 1; white-space: nowrap;
  }

  .contact-list {
    position: absolute;
    display: grid; grid-template-columns: auto auto;
    column-gap: 10px; row-gap: 3px;
    color: var(--paper); font-size: 12px; line-height: 16px;
    white-space: nowrap;
  }
  .contact-list dt { font-style: italic; text-align: right; }
  .contact-list dd { font-weight: 700; }

  /* Front 1 */
  .front-one { top: 43px; }
  .front-one .brand-name { left: 32px; top: 110px; }
  .front-one .service-word { left: 258px; top: 80px; font-size: 30px; }
  .front-one .contact-list { left: 176px; top: 203px; }

  /* Front 2 */
  .front-two { top: 459px; }
  .front-two .brand-name { left: 40px; top: 78px; font-size: 28px; }
  .service-tab {
    position: absolute; left: 210px; top: 162px;
    width: 160px; height: 38px;
    background: var(--brand-blue); border-radius: 7px 7px 0 0;
    display: flex; align-items: center; justify-content: center;
  }
  .service-tab .service-word { position: static; font-size: 27px; }
  .front-two .contact-list { left: 176px; top: 203px; }

  /* Back */
  .back { top: 857px; }
  .back-copy {
    position: absolute; inset: 0;
    color: var(--paper); text-align: center;
  }
  .tagline {
    position: absolute; left: 0; right: 0; top: 50px;
    font-family: "Russo One", "Arimo", sans-serif;
    font-size: 20px; font-weight: 400; letter-spacing: 0.5px;
  }
  .services {
    position: absolute; left: 0; right: 0; top: 103px;
    font-size: 14px; line-height: 20px; list-style: none;
  }
  .call-to-action {
    position: absolute; left: 0; right: 0; top: 220px;
    font-size: 14px; font-weight: 700; line-height: 18px;
  }
</style>
</head>
<body>
<main class="sheet">

  <span class="side-label" style="top:165px">front 1</span>
  <span class="side-label" style="top:606px">front 2</span>
  <span class="side-label" style="top:998px">back</span>

  <!-- Front 1 -->
  <section class="card front-one" aria-label="Business card front, version 1">
    <svg class="card-art" viewBox="0 0 346 228" preserveAspectRatio="none" aria-hidden="true">
      <rect width="346" height="228" fill="var(--brand-blue)"/>
      <circle cx="-10" cy="-10" r="206" fill="var(--ring-blue)"/>
      <circle cx="-10" cy="-10" r="196" fill="var(--paper)"/>
    </svg>
    <span class="brand-name">Owen Daley</span>
    <span class="service-word">FITNESS</span>
    <dl class="contact-list">
      <dt>email</dt><dd>owendaleyfitness.example.co.uk</dd>
      <dt>phone</dt><dd>07700954218</dd>
      <dt>facebook</dt><dd>owendaleyfitness</dd>
      <dt>twitter</dt><dd>@owendaleyfitness</dd>
    </dl>
  </section>

  <!-- Front 2 -->
  <section class="card front-two" aria-label="Business card front, version 2">
    <svg class="card-art" viewBox="0 0 346 228" preserveAspectRatio="none" aria-hidden="true">
      <rect width="346" height="228" fill="var(--paper)"/>
      <rect y="156" width="346" height="72" fill="var(--brand-blue)"/>
      <rect y="221" width="346" height="7" fill="var(--ring-blue)"/>
    </svg>
    <span class="brand-name">Owen Daley</span>
    <div class="service-tab"><span class="service-word">FITNESS</span></div>
    <dl class="contact-list">
      <dt>email</dt><dd>owendaleyfitness.example.co.uk</dd>
      <dt>phone</dt><dd>07700954218</dd>
      <dt>facebook</dt><dd>owendaleyfitness</dd>
      <dt>twitter</dt><dd>@owendaleyfitness</dd>
    </dl>
  </section>

  <!-- Back -->
  <section class="card back" aria-label="Business card back">
    <svg class="card-art" viewBox="0 0 346 228" preserveAspectRatio="none" aria-hidden="true">
      <defs>
        <clipPath id="back-panel-clip"><rect x="5" y="7" width="334" height="215"/></clipPath>
      </defs>
      <rect x="5" y="7" width="334" height="215" fill="var(--brand-blue)"/>
      <g clip-path="url(#back-panel-clip)">
        <circle cx="173" cy="115" r="107" fill="none" stroke="var(--soft-blue)" stroke-width="38" opacity="0.85"/>
      </g>
      <g fill="none" stroke="var(--paper)" stroke-width="0.8">
        <path d="M12 44 V12 H335"/>
        <path d="M16 40 V16 H330"/>
        <path d="M330 180 V216 H200"/>
        <path d="M335 176 V220"/>
      </g>
    </svg>
    <div class="back-copy">
      <h1 class="tagline">REAL RESULTS FOR EVERY BODY</h1>
      <ul class="services">
        <li>specializing in :</li>
        <li>- weight loss &amp; tone</li>
        <li>- strength and conditioning</li>
        <li>- nutritional advice</li>
      </ul>
      <p class="call-to-action">Book your free consultation today<br>and take the first step toward achieving your goal!</p>
    </div>
  </section>

</main>
</body>
</html>
```